Etiketten-Design für Rotwein
Zielgruppe
Weinkellerei aus Baden (Deutschland) mit Fokus im Lebensmittelhandel in Deutschland
Aufgabenstellung
Wir suchen ein Frontetikett für einen modernen badischen Rotwein (Cuvée Noir) mit dem Namen 'The ember hour of Wielgrund'
Aus dem Etikett soll hervorgehen, dass es sich nicht um einen klassischen, leichten deutschen Rotwein handelt, sondern um einen kräftigen, gehaltvollen, mediterran anmutenden Rotwein mit purpurroter Farbe und vollmundigem, nachhaltigem Geschmack. (Geschmacksrichtung feinherb)
Zielgruppe Discount-Kunden, Männlich/Weiblich, Alter: 25-60 Jahre, wird für unter € 5,-/Fl. verkauft.
Weinbeschreibung:
Farbe: Ein wunderschönes tiefdunkles purpurrot mit violetten Reflexen
Duft: In der Nase zeigen sich Aromen nach Waldbeeren, sowie Anklänge von Rauch, Röstaromen, Nelke, etwas Vanille und dunkle Schokolade
Geschmack: Geschmacklich füllig und kraftvoll, Brombeeraromen und schön eingebundenen Tanninen. Langanhaltend intensiv im Abgang.
Anforderungen Etikett:
Maße: Höhe max. 120mm/Breite max. 80mm (darf auch kleiner oder quadratisch sein)
SK Etikett, Naturstruktur bis 90g (m²) (Ein - oder zweiteilig)
Eine figürliche Etikettenkontur ist möglich, es wird aber am rechten Etikettenrand eine gerade Spendekante benötigt um das Etikett maschinell verarbeiten zu können.
Als Flasche wird eine 0,75 L Bordeauxflasche (Farbe: grün) eingesetzt.
Verschluss: Longcap
Mögliche Veredelungen: Quelllack, Prägungen, Heissfolie, Glanzlack
Pflichtangaben:
The ember hour of Wielgrund

```html
<!DOCTYPE html>
<html lang="de">
<head>
<meta charset="utf-8">
<title>The ember hour of Wielgrund – Frontetikett</title>
<link rel="stylesheet" href="https://fonts.googleapis.com/css2?family=Work+Sans:wght@400&display=swap">
<style>
  :root {
    --backdrop: #0c0c0e;
    --label-plum: #4b1b2c;
    --label-wine: #36142a;
    --label-night: #17181f;
    --title: #e6e2e5;
    --copy: #8e7f8a;
    --rule: #6e5a66;
  }
  * { margin: 0; padding: 0; box-sizing: border-box; }
  html, body {
    width: 1000px;
    height: 1200px;
    overflow: hidden;
    background: var(--backdrop);
  }
  .label {
    position: absolute;
    left: 238px;
    top: 100px;
    width: 524px;
    height: 1000px;
    background:
      radial-gradient(ellipse 70% 45% at 0% 100%, rgba(80, 22, 44, 0.55), transparent 70%),
      linear-gradient(125deg, var(--label-plum) 0%, var(--label-wine) 35%, var(--label-night) 78%, var(--label-night) 100%);
    font-family: "Work Sans", sans-serif;
    font-weight: 400;
  }
  .wine-name {
    position: absolute;
    left: 51px;
    right: 51px;
    top: 200px;
    color: var(--title);
    font-size: 60px;
    font-weight: 400;
    line-height: 76px;
    letter-spacing: 0;
  }
  .tasting-notes {
    position: absolute;
    left: 51px;
    right: 51px;
    top: 650px;
    color: var(--copy);
    font-size: 19px;
    line-height: 28px;
    text-align: justify;
    hyphens: auto;
    -webkit-hyphens: auto;
  }
  .tasting-notes .rule {
    width: 205px;
    height: 1px;
    background: var(--rule);
  }
  .tasting-notes .rule.top { margin-bottom: 20px; }
  .tasting-notes .rule.bottom { margin-top: 12px; }
  .tasting-notes p + p { margin-top: 28px; }
</style>
</head>
<body>
  <main class="label" aria-label="Frontetikett The ember hour of Wielgrund">
    <h1 class="wine-name">The ember<br>hour of<br>Wielgrund</h1>
    <section class="tasting-notes">
      <div class="rule top"></div>
      <p>Aromen: Waldbeeren, Anklänge von Rauch, Röstaromen, Nelke, etwas Vanille und dunkle Schokolade.</p>
      <p>Geschmack: Füllig und kraftvoll, Brombeeraromen und schön eingebundene Tannine. Langanhaltend intensiv im Abgang.</p>
      <div class="rule bottom"></div>
    </section>
  </main>
</body>
</html>
```